Chiropractic healthcare group business card

We are a Portland Oregon based chiropractic healthcare group. Looking for a new business card design. Something cutting edge, that shows off our new logo and tag line.Use either of the attached logos.Our tag line = "Who would you be without pain?"I'm open to about anything, impress me!!
Target Market(s)
Chiropractic patients - Auto injury, back pain, sports injuries, neck , shoulder, hip, knee, ankle pain.
Industry/Entity Type
Chiropractic
Contact Information for Business Card
Dr. Bram Holtvick, D.C.
Clinic name - Fernway Chiropractic
2 clinics
location #1
20418 NW Marwick Road
Suite B
North Plains, OR 97133
Location #2
13529 SE Calloway Street
Portland OR 97236
Main phone line 971.555.0143
website : www.FernwayClinics.example
Tag line "Who would you be without pain?"
Colors
Designer to choose colors to be used in the design.
Requirements
Must have
- Use the logo colors -- Want the orange color to be a TRUE orange.
- Both clinic address
- phone number
- website
- personal email - b.holtvick@ReliefBeginsHere.example
- tag line - "Who would you be without pain?"

```html
<!DOCTYPE html>
<html lang="en">
<head>
<meta charset="UTF-8">
<title>Fernway Chiropractic – Business Card</title>
<link rel="stylesheet" href="https://fonts.googleapis.com/css2?family=Open+Sans:wght@400;600;700&display=swap">
<style>
  :root {
    --bg: #e4e4e4;
    --card-dark: #58595b;
    --card-light: #f0f0f0;
    --orange: #f47b20;
    --ink: #4a4a4c;
    --white: #ffffff;
  }
  * { margin: 0; padding: 0; box-sizing: border-box; }
  html, body {
    width: 1200px; height: 1021px; overflow: hidden;
    background: var(--bg);
    font-family: "Open Sans", Arial, sans-serif;
  }
  .card {
    position: absolute; left: 260px;
    width: 680px; height: 380px;
    box-shadow: 0 4px 14px rgba(0,0,0,0.18);
  }
  .card-front { top: 105px; background: var(--card-dark); }
  .card-back { top: 535px; background: var(--card-light); color: var(--ink); }

  /* front */
  .brand {
    position: absolute; left: 0; right: 0; top: 92px;
    text-align: center; color: var(--white); font-weight: 700;
  }
  .brand-mark {
    width: 22px; height: 22px; border-radius: 50%;
    background: var(--orange); margin: 0 auto 18px;
  }
  .brand-name { font-size: 58px; letter-spacing: 22px; line-height: 1; padding-left: 22px; }
  .brand-sub { font-size: 22px; letter-spacing: 9px; margin-top: 10px; padding-left: 9px; }
  .tagline {
    position: absolute; left: 0; right: 0; top: 290px;
    text-align: center; color: var(--white);
    font-size: 19px; font-weight: 600; letter-spacing: 0.5px;
  }
  .tagline em { font-style: normal; color: var(--orange); }

  /* back */
  .person {
    position: absolute; right: 392px; top: 78px; text-align: right;
  }
  .person-name { color: var(--orange); font-weight: 700; font-size: 22px; }
  .person-role { font-size: 19px; margin-top: 2px; }
  .divider {
    position: absolute; left: 310px; top: 80px;
    width: 2px; height: 78px; background: var(--ink);
  }
  .contacts {
    position: absolute; left: 330px; top: 82px;
    list-style: none; font-size: 16px; line-height: 25px;
  }
  .contacts li { display: flex; align-items: center; gap: 8px; }
  .contacts svg { width: 15px; height: 15px; flex: none; }
  .back-brand {
    position: absolute; left: 0; right: 0; top: 214px;
    text-align: center; color: var(--orange);
    font-size: 13px; font-weight: 700; letter-spacing: 2px;
  }
  .addresses {
    position: absolute; left: 0; right: 0; top: 244px;
    text-align: center; font-size: 18px; line-height: 26px;
  }
</style>
</head>
<body>
  <section class="card card-front">
    <div class="brand">
      <div class="brand-mark"></div>
      <div class="brand-name">FERNWAY</div>
      <div class="brand-sub">CHIROPRACTIC</div>
    </div>
    <p class="tagline">WHO WOULD YOU BE <em>WITHOUT PAIN?</em></p>
  </section>

  <section class="card card-back">
    <div class="person">
      <div class="person-name">Dr. Bram Holtvick, D.C.</div>
      <div class="person-role">Founder</div>
    </div>
    <div class="divider"></div>
    <ul class="contacts">
      <li>
        <svg viewBox="0 0 16 16" aria-hidden="true"><path fill="var(--orange)" d="M3.6 1.2l2.2 2.7-1.3 1.9c.9 2 2.6 3.8 4.7 4.7l1.9-1.3 2.7 2.2-1.2 2.4C7.2 13.6 2.4 8.8 1.2 3.4z"/></svg>
        971.555.0143
      </li>
      <li>
        <svg viewBox="0 0 16 16" aria-hidden="true"><rect x="1.5" y="3.5" width="13" height="9" fill="none" stroke="var(--orange)" stroke-width="1.6"/><path d="M1.5 3.5L8 9l6.5-5.5" fill="none" stroke="var(--orange)" stroke-width="1.6"/></svg>
        b.holtvick@ReliefBeginsHere.example
      </li>
      <li>
        <svg viewBox="0 0 16 16" aria-hidden="true"><g fill="none" stroke="var(--orange)" stroke-width="1.3"><circle cx="8" cy="8" r="6.3"/><ellipse cx="8" cy="8" rx="2.8" ry="6.3"/><path d="M1.7 8h12.6M2.8 4.8h10.4M2.8 11.2h10.4"/></g></svg>
        www.FernwayClinics.example
      </li>
    </ul>
    <div class="back-brand">FERNWAY CHIROPRACTIC</div>
    <address class="addresses" style="font-style:normal">
      20418 NW Marwick Road, Suite B, North Plains, OR 97133<br>
      13529 SE Calloway Street, Portland OR 97236
    </address>
  </section>
</body>
</html>
```